Healthcare website - Diabetic Shoes - Elderfund - No Cost

I am looking to upgrade my website. I do not want to use Wordpress, Adobe Muse or another designing program. The code should be easily editable using textpad or VI. After the project is done I want to easily add my custom PHP code.

Features
Creative and Modern Design .
Fully responsive site for use on mobile devices
bootstrap, jquery

My current website is
www.pebblewalkco.com

Target Market(s)

Older people who have diabetes. Target market is +60 years old, but we do have younger people going to the site to help out their parents.

Industry/Entity Type

Healthcare

Coding

Coded - Design and coding required

Number of Pages Required

2 page

Colors

Designer to choose colors to be used in the design.

Requirements
Must have
• The code should be easily editable using textpad or VI. After the project is done I want to easily add my custom PHP code.
• The first page will be the home page and the other page I need is this form.
• https://www.pebblewalkco.com/pebble-walk-co-do-i-qualify.php
Should not have
• I do not want to use Wordpress, Adobe Muse or another designing program.

```html
<!DOCTYPE html>
<html lang="en">
<head>
<meta charset="utf-8">
<title>Pebble Walk Co – Diabetic Shoes Covered By Elderfund</title>
<link rel="stylesheet" href="https://fonts.googleapis.com/css2?family=Raleway:wght@400;500;600;700&display=swap">
<style>
:root{
  --green:#6cbf4f;
  --green-dark:#5aad3e;
  --blue:#4c7eb0;
  --blue-deep:#4a77a6;
  --title-blue:#3f74a8;
  --text:#5b5b5b;
  --muted:#8a8a8a;
  --line:#dcdcdc;
  --panel:#f3f3f3;
  --white:#ffffff;
}
*{box-sizing:border-box;margin:0;padding:0}
html,body{width:1200px;height:5114px;overflow:hidden}
body{font-family:"Raleway",sans-serif;color:var(--text);background:var(--white);position:relative}
a{text-decoration:none}
section,header,footer{position:absolute;left:0;width:1200px}
.abs{position:absolute}

/* header */
.site-header{top:0;height:136px;background:var(--white)}
.brand{left:78px;top:44px;display:flex;align-items:center;gap:10px;font-size:30px;font-weight:700;color:var(--title-blue)}
.brand-dot{width:14px;height:14px;border-radius:50%;background:var(--green)}
.main-nav{right:75px;top:56px;display:flex;gap:20px;font-size:15px;font-weight:500}
.main-nav a{color:var(--text)}
.main-nav a.active{color:var(--green)}

/* hero */
.hero{top:136px;height:522px;background:linear-gradient(90deg,#bcb3a8 0%,#cfc7bc 55%,#b2a597 100%)}
.hero-photo{right:60px;top:30px;width:560px;height:470px;border-radius:4px;background:radial-gradient(ellipse at 55% 55%,#8a6a4c 0%,#6a5847 40%,rgba(160,150,140,0) 72%)}
.hero-title{left:78px;top:104px;font-size:41px;font-weight:600;line-height:1.15;color:var(--white)}
.hero-text{left:78px;top:222px;width:410px;font-size:13px;line-height:1.6;color:var(--white)}
.btn{display:inline-block;background:var(--green);color:var(--white);text-align:center;font-weight:500}
.hero-btn{left:78px;top:358px;width:195px;height:46px;line-height:46px;font-size:17px}

/* about + philosophy */
.intro{top:658px;height:399px;display:flex}
.intro-col{position:relative;width:600px;height:399px}
.intro-about{background:var(--blue)}
.intro-philosophy{background:var(--green)}
.intro-title{position:absolute;top:52px;left:0;width:100%;text-align:center;font-size:30px;font-weight:500;color:var(--white)}
.intro-title::after{content:"";display:block;width:40px;height:2px;background:var(--white);margin:12px auto 0}
.intro-img{position:absolute;top:147px;width:178px;height:185px}
.intro-about .intro-img{left:78px;background:linear-gradient(160deg,#dfe6ee,#9fb2c4 60%,#6e8a6a)}
.intro-philosophy .intro-img{left:38px;background:linear-gradient(160deg,#dfe9f2,#8fa9c2 55%,#4e6a88)}
.intro-text{position:absolute;top:147px;font-size:13px;line-height:1.55;color:var(--white)}
.intro-about .intro-text{left:273px;width:305px}
.intro-philosophy .intro-text{left:252px;width:305px}
.intro-text a{color:var(--white);font-weight:600}

/* shoes */
.shoes{height:420px}
.mens{top:1057px}
.womens{top:1450px;height:391px}
.section-title{position:absolute;left:0;width:1200px;text-align:center;font-size:30px;font-weight:500;color:var(--title-blue)}
.section-title::after{content:"";display:block;width:40px;height:2px;background:var(--green);margin:14px auto 0}
.shoe-card{position:absolute;width:177px;height:157px;border:2px solid var(--line);background:var(--white)}
.shoe-img{position:absolute;left:24px;top:42px;width:125px;height:70px;border-radius:40% 50% 20% 20%}

/* steps */
.steps{top:1841px;height:1160px;background:var(--panel)}
.step-text{font-size:25px;line-height:1.4;color:#444;white-space:nowrap}
.step-icon{width:52px;height:60px}

/* faq */
.faq{top:3001px;height:784px;background:var(--white)}
.faq-q{left:165px;width:870px;font-size:16px;font-weight:500;color:var(--green-dark)}
.faq-a{left:165px;width:870px;font-size:13px;line-height:1.75;color:var(--text)}

/* products */
.products{top:3785px;height:529px;background:var(--panel)}
.product-card{position:absolute;top:181px;width:239px;height:262px;border:2px solid #c8ced6;background:var(--white)}
.product-img{position:absolute;left:40px;top:30px;width:155px;height:196px;border-radius:10px}

/* form */
.catalog{top:4314px;height:569px;background:var(--white)}
.field{position:absolute;width:321px;height:40px;border:1px solid #e2e2e2;background:#fafafa;font-size:13px;color:var(--muted);padding:0 14px;line-height:38px}
.form-btn{position:absolute;width:317px;height:40px;line-height:40px;font-size:16px}

/* partner strip */
.partners{top:4883px;height:123px;background:#f6f6f6;display:flex;justify-content:center;align-items:center;gap:60px}

/* footer */
.site-footer{top:5006px;height:108px;background:var(--blue-deep);color:var(--white);font-size:13px}
.site-footer .abs{top:46px;white-space:nowrap}
</style>
</head>
<body>

<header class="site-header">
  <div class="brand abs"><span class="brand-dot"></span>Pebble Walk Co</div>
  <nav class="main-nav abs">
    <a class="active" href="#">Home</a><a href="#">About</a><a href="#">Why Diabetic Shoes</a><a href="#">Shoes</a><a href="#">All Products</a><a href="#">Shoe Fitter Jobs</a><a href="#">FAQ</a>
  </nav>
</header>

<section class="hero">
  <div class="hero-photo abs" role="img" aria-label="Leather chukka boots and a grey sneaker"></div>
  <h1 class="hero-title abs">Diabetic Shoes Or Sneakers<br>Covered By Elderfund</h1>
  <p class="hero-text abs">No or little out of pocket cost to you! Elderfund and most insurance plans may cover the cost of one pair of diabetic shoes and three pairs of custom inserts per calendar year. Co-payments, deductibles and some restrictions apply.</p>
  <a class="btn hero-btn abs" href="#">Shop Now</a>
</section>

<section class="intro">
  <div class="intro-col intro-about">
    <h2 class="intro-title">About Us</h2>
    <div class="intro-img" role="img" aria-label="Office building of the company"></div>
    <p class="intro-text">Pebble Walk Co was created by Brightstep Medical Supply to educate clients and prospective shoe fitters about diabetic shoes and the coverage that Elderfund provides. Founded by a Board-Certified Pedorthist, the company's mission is to help clients receive properly fitted shoes from qualified healthcare professionals around the United States. <a href="#">Read More</a></p>
  </div>
  <div class="intro-col intro-philosophy">
    <h2 class="intro-title">Our Philosophy</h2>
    <div class="intro-img" role="img" aria-label="Healthcare professionals at work"></div>
    <p class="intro-text">At Brightstep Medical Supply, we understand the health benefits and medical safety associated with properly fitted shoes. We strive to educate clients about wearing appropriate footwear and avoiding unnecessary complications. One in four Americans with diabetes will develop potentially serious foot problems related to disease. <a href="#">Read More</a></p>
  </div>
</section>

<section class="shoes mens">
  <h2 class="section-title" style="top:69px">Men's Shoes</h2>
  <div class="shoe-card" style="left:78px;top:188px"><div class="shoe-img" role="img" aria-label="Black men's walking shoe" style="background:linear-gradient(#3a3a3a,#1d1d1d)"></div></div>
  <div class="shoe-card" style="left:297px;top:188px"><div class="shoe-img" role="img" aria-label="Navy men's sneaker" style="background:linear-gradient(#3f4f66,#1f2a3a)"></div></div>
  <div class="shoe-card" style="left:512px;top:188px"><div class="shoe-img" role="img" aria-label="Grey men's sneaker" style="background:linear-gradient(#8b8f93,#5a5e62)"></div></div>
  <div class="shoe-card" style="left:726px;top:188px"><div class="shoe-img" role="img" aria-label="Black men's athletic shoe" style="background:linear-gradient(#3a3a3a,#151515)"></div></div>
  <div class="shoe-card" style="left:941px;top:188px"><div class="shoe-img" role="img" aria-label="Black men's strap shoe" style="background:linear-gradient(#444,#1a1a1a)"></div></div>
</section>

<section class="shoes womens">
  <h2 class="section-title" style="top:36px">Women's Shoes</h2>
  <div class="shoe-card" style="left:78px;top:146px"><div class="shoe-img" role="img" aria-label="Black women's slip-on shoe" style="background:linear-gradient(#3a3a3a,#1b1b1b)"></div></div>
  <div class="shoe-card" style="left:297px;top:146px"><div class="shoe-img" role="img" aria-label="Turquoise women's sneaker" style="background:linear-gradient(#7fd2cf,#4aa6a3)"></div></div>
  <div class="shoe-card" style="left:512px;top:146px"><div class="shoe-img" role="img" aria-label="Brown women's mary jane shoe" style="background:linear-gradient(#9a5a32,#6b3a1e)"></div></div>
  <div class="shoe-card" style="left:726px;top:146px"><div class="shoe-img" role="img" aria-label="Black women's walking shoe" style="background:linear-gradient(#3f3f3f,#1c1c1c)"></div></div>
  <div class="shoe-card" style="left:941px;top:146px"><div class="shoe-img" role="img" aria-label="Black women's strap shoe" style="background:linear-gradient(#454545,#1e1e1e)"></div></div>
</section>

<section class="steps">
  <h2 class="section-title" style="top:64px">4 Easy Steps To Receive Your New Therapeutic Shoes</h2>

  <svg class="step-icon abs" style="left:185px;top:262px" viewBox="0 0 52 60" aria-hidden="true">
    <path d="M4 2h30l14 14v42H4z" fill="var(--blue)"/><path d="M34 2v14h14" fill="#8fb0d0"/>
    <rect x="12" y="26" width="28" height="3" fill="#fff"/><rect x="12" y="34" width="28" height="3" fill="#fff"/><rect x="12" y="42" width="20" height="3" fill="#fff"/>
  </svg>
  <p class="step-text abs" style="left:268px;top:252px">Fill out an application<br>to see if you qualify.</p>
  <div class="abs" role="img" aria-label="Hand signing an application form" style="left:675px;top:194px;width:320px;height:198px;background:linear-gradient(135deg,#eef3f8,#b8c9dc)"></div>

  <div class="abs" role="img" aria-label="Stethoscope on a desk with documents" style="left:188px;top:416px;width:324px;height:198px;background:linear-gradient(135deg,#cfe0ee,#5d85ad)"></div>
  <svg class="step-icon abs" style="left:665px;top:484px" viewBox="0 0 52 60" aria-hidden="true">
    <rect x="4" y="6" width="44" height="52" rx="3" fill="var(--blue)"/><rect x="16" y="2" width="20" height="9" rx="2" fill="#2f5c8a"/>
    <rect x="12" y="22" width="28" height="3" fill="#fff"/><rect x="12" y="31" width="28" height="3" fill="#fff"/><rect x="12" y="40" width="18" height="3" fill="#fff"/>
  </svg>
  <p class="step-text abs" style="left:742px;top:466px">A prescription will be<br>faxed to your primary<br>physician.</p>

  <svg class="step-icon abs" style="left:178px;top:708px" viewBox="0 0 52 60" aria-hidden="true">
    <path d="M2 40c0-8 4-14 8-16l6 6 10-2 12 8c8 2 12 4 12 8v4H2z" fill="var(--blue)"/>
  </svg>
  <p class="step-text abs" style="left:268px;top:684px">After the prescription<br>is signed, a certified shoe<br>fitter will fit your new<br>shoes.</p>
  <div class="abs" role="img" aria-label="Brown leather dress shoe" style="left:675px;top:658px;width:320px;height:198px;background:radial-gradient(ellipse at 50% 60%,#8a4a22,#5a2c12 45%,#e9e4df 75%)"></div>

  <div class="abs" role="img" aria-label="Shoe fitter greeting a happy client" style="left:188px;top:880px;width:324px;height:198px;background:linear-gradient(135deg,#d9c7b6,#7d6a5b)"></div>
  <svg class="step-icon abs" style="left:665px;top:946px" viewBox="0 0 52 60" aria-hidden="true">
    <rect x="4" y="16" width="44" height="34" rx="4" fill="var(--blue)"/><rect x="18" y="8" width="16" height="10" rx="2" fill="none" stroke="var(--blue)" stroke-width="4"/>
    <path d="M16 33l7 7 13-13" fill="none" stroke="#fff" stroke-width="4"/>
  </svg>
  <p class="step-text abs" style="left:742px;top:936px">Enjoy your new<br>shoes!</p>
</section>

<section class="faq">
  <h2 class="section-title" style="top:68px">Frequently Asked Questions</h2>
  <h3 class="faq-q abs" style="top:199px">1. How Does Diabetes Cause Foot Problems?</h3>
  <p class="faq-a abs" style="top:232px">Diabetes can cause neuropathy, nerve damage which reduces feeling in your feet. This makes you less likely to feel the early warning signs of foot problems. Decreased circulation reduces the ability to heal and fight off infection. These two conditions significantly increase the likelihood of foot complications, infection and ulceration.</p>
  <h3 class="faq-q abs" style="top:358px">2. Why Are Properly Fitted Shoes Important?</h3>
  <p class="faq-a abs" style="top:391px">Twenty five million people have diabetes, and twenty five percent of this population will develop foot problems caused by their disease. We provide the most fashionable orthopedic shoes available in a variety of styles and brands to help treat and prevent painful diabetic symptoms.</p>
  <p class="faq-a abs" style="top:472px">Our orthopedic shoes reduce the pressure and friction on your feet that can lead to foot injuries. Custom inserts relieve pressure and cushion your feet. Diabetic socks and our therapeutic shoes are also lined with soft padding to ensure there is enough room in the toe box, heel and arch of the shoe. All of these features provide you with the very best in comfort and help prevent foot complications.</p>
  <h3 class="faq-q abs" style="top:589px">3. How Do You Know If Orthopedic Shoes Are Right For You?</h3>
  <p class="faq-a abs" style="top:622px">Anyone with Diabetic Neuropathy, poor circulation, high risk of infection or nerve damage can benefit from diabetic socks and our shoes. Elderfund patients who qualify are eligible for one pair of shoes and three pairs of custom insoles per year – at no out of pocket cost to them. Additionally, most private insurance companies will cover the same benefits as Elderfund.</p>
</section>

<section class="products">
  <h2 class="section-title" style="top:85px">Click Here For Our Elderfund Products</h2>
  <div class="product-card" style="left:78px"><div class="product-img" role="img" aria-label="TENS therapy unit with electrode pads" style="background:linear-gradient(#f2f2f2,#3a3a3a 55%,#e6e6e6)"></div></div>
  <div class="product-card" style="left:348px"><div class="product-img" role="img" aria-label="Black knee brace" style="background:radial-gradient(ellipse,#2e2e2e 45%,#fff 72%)"></div></div>
  <div class="product-card" style="left:614px"><div class="product-img" role="img" aria-label="Blue and grey back support" style="background:linear-gradient(160deg,#cfd8e2,#3f6d9c 55%,#9aa4ad)"></div></div>
  <div class="product-card" style="left:880px"><div class="product-img" role="img" aria-label="Black wrist and ankle braces" style="background:linear-gradient(120deg,#fff,#2a2a2a 45%,#555 70%,#fff)"></div></div>
</section>

<section class="catalog">
  <h2 class="section-title" style="top:85px">Request A Free Diabetic Shoe Catalog</h2>
  <div class="field" style="left:266px;top:187px">Name</div>
  <div class="field" style="left:614px;top:187px">Phone</div>
  <div class="field" style="left:266px;top:242px">Address</div>
  <div class="field" style="left:614px;top:242px">City</div>
  <div class="field" style="left:266px;top:297px">State</div>
  <div class="field" style="left:614px;top:297px">Zip</div>
  <div class="field" style="left:266px;top:352px">Email</div>
  <div class="field" style="left:614px;top:352px">Best time to Call</div>
  <div class="field" style="left:266px;top:407px">Primary Insurance</div>
  <div class="field" style="left:614px;top:407px">Do you want to check eligibility Online?</div>
  <div class="field" style="left:266px;top:462px">Comments</div>
  <a class="btn form-btn" href="#" style="left:614px;top:462px">Request Catalog</a>
</section>

<section class="partners" aria-label="Partners and certifications">
  <div style="width:60px;height:60px;background:#3f6b3a"></div>
  <div style="width:80px;height:50px;background:#cfd3d8"></div>
  <div style="width:90px;height:56px;border-radius:50%;background:#2f4f86"></div>
  <div style="width:110px;height:36px;background:#d9d9d9"></div>
</section>

<footer class="site-footer">
  <div class="abs" style="left:78px">Terms of Use &nbsp;|&nbsp; Privacy Policy &nbsp;|&nbsp; Returns/Exchanges</div>
  <div class="abs" style="left:430px">*Co-payments, deductibles and some restrictions apply.</div>
  <div class="abs" style="right:78px">© Copyright Pebble Walk Co - All Rights Reserved.</div>
</footer>

</body>
</html>
```